Velmorfood

We produce juices. We need a label design for 300ml and 1L bottles. Our company's name is "Velmor food", In honor of Aragats mountain. If we like some of the examples, in future for the final result we will send Armenian version of company's name in armenian letters.

Industry/Entity Type

It Company

```html
<!DOCTYPE html>
<html lang="en">
<head>
<meta charset="utf-8">
<title>Velmor food – juice labels</title>
<link rel="stylesheet" href="https://fonts.googleapis.com/css2?family=Encode+Sans+Condensed:wght@400&family=Open+Sans:wght@300;600&family=Marcellus+SC&family=Caveat+Brush&family=Fondamento&display=swap">
<style>
  :root {
    --orange: #ff8a00;
    --yellow: #ffec00;
    --red: #d50000;
    --green: #00ff6e;
    --white: #ffffff;
    --berry: #a30000;
    --ink: #111111;
    --page: #ffffff;
  }
  html, body {
    margin: 0;
    width: 1200px;
    height: 535px;
    overflow: hidden;
    background: var(--page);
  }
  .label-set {
    position: relative;
    width: 1200px;
    height: 535px;
  }
  .label {
    position: absolute;
    top: 20px;
    width: 275px;
    height: 492px;
    border-radius: 18px;
    background: var(--tone);
    color: var(--white);
  }
  .label--orange { left: 23px;  --tone: var(--orange); --accent: var(--berry); }
  .label--yellow { left: 316px; --tone: var(--yellow); --accent: var(--berry); }
  .label--red    { left: 609px; --tone: var(--red);    --accent: var(--ink); }
  .label--green  { left: 901px; --tone: var(--green);  --accent: var(--berry); }

  .badge {
    position: absolute;
    left: 0;
    top: 0;
    width: 275px;
    height: 300px;
  }
  .badge__ring { fill: none; stroke: var(--white); stroke-width: 4; }
  .badge__disc { fill: var(--white); }
  .brand {
    fill: var(--tone);
    font-family: "Encode Sans Condensed", sans-serif;
    font-weight: 400;
  }
  .brand__name { font-size: 62px; }
  .brand__product { font-size: 108px; }

  .flavours {
    position: absolute;
    left: 0;
    top: 312px;
    width: 275px;
    margin: 0;
    padding: 0;
    list-style: none;
    text-align: center;
    font-size: 20px;
    line-height: 20px;
    white-space: nowrap;
  }
  .flavours li { height: 20px; }
  .f-serif  { font-family: "Marcellus SC", serif; font-size: 20px; }
  .f-sans   { font-family: "Open Sans", sans-serif; font-weight: 600; font-size: 17px; }
  .f-light  { font-family: "Open Sans", sans-serif; font-weight: 300; font-size: 17px; letter-spacing: 1px; }
  .f-brush  { font-family: "Caveat Brush", cursive; font-size: 22px; letter-spacing: 1px; }
  .f-old    { font-family: "Fondamento", cursive; font-size: 19px; }
  .f-accent { color: var(--accent); font-family: "Open Sans", sans-serif; font-weight: 400; font-size: 17px; }

  .rule {
    position: absolute;
    left: 29px;
    top: 458px;
    width: 219px;
    height: 2px;
    background: var(--white);
  }
</style>
</head>
<body>
<main class="label-set">

  <section class="label label--orange">
    <svg class="badge" viewBox="0 0 275 300">
      <circle class="badge__ring" cx="137.5" cy="145" r="127"/>
      <circle class="badge__disc" cx="137.5" cy="145" r="119"/>
      <text class="brand brand__name" x="137.5" y="134" text-anchor="middle" textLength="150" lengthAdjust="spacingAndGlyphs">velmor</text>
      <text class="brand brand__product" x="137.5" y="221" text-anchor="middle" textLength="184" lengthAdjust="spacingAndGlyphs">JUICES</text>
    </svg>
    <ul class="flavours">
      <li><span class="f-serif">KIWI</span> <span class="f-sans">ORANGE</span> <span class="f-brush">APPLE</span></li>
      <li><span class="f-serif">STRAWBERRY</span> <span class="f-serif">BLUEBERRY</span></li>
      <li><span class="f-old">Avocado</span> <span class="f-light">CITRUS</span> <span class="f-brush">GRAPE</span></li>
      <li><span class="f-serif">COCONUT</span> <span class="f-accent">CRANBERRY</span></li>
      <li><span class="f-old">MANGO</span> <span class="f-serif">MELON</span> <span class="f-sans">PEACH</span></li>
      <li><span class="f-brush">PINEAPPLE</span> <span class="f-light">PAPAYA</span></li>
    </ul>
    <div class="rule"></div>
  </section>

  <section class="label label--yellow">
    <svg class="badge" viewBox="0 0 275 300">
      <circle class="badge__ring" cx="137.5" cy="145" r="127"/>
      <circle class="badge__disc" cx="137.5" cy="145" r="119"/>
      <text class="brand brand__name" x="137.5" y="134" text-anchor="middle" textLength="150" lengthAdjust="spacingAndGlyphs">velmor</text>
      <text class="brand brand__product" x="137.5" y="221" text-anchor="middle" textLength="184" lengthAdjust="spacingAndGlyphs">JUICES</text>
    </svg>
    <ul class="flavours">
      <li><span class="f-serif">KIWI</span> <span class="f-sans">ORANGE</span> <span class="f-brush">APPLE</span></li>
      <li><span class="f-serif">STRAWBERRY</span> <span class="f-serif">BLUEBERRY</span></li>
      <li><span class="f-old">Avocado</span> <span class="f-light">CITRUS</span> <span class="f-brush">GRAPE</span></li>
      <li><span class="f-serif">COCONUT</span> <span class="f-accent">CRANBERRY</span></li>
      <li><span class="f-old">MANGO</span> <span class="f-serif">MELON</span> <span class="f-sans">PEACH</span></li>
      <li><span class="f-brush">PINEAPPLE</span> <span class="f-light">PAPAYA</span></li>
    </ul>
    <div class="rule"></div>
  </section>

  <section class="label label--red">
    <svg class="badge" viewBox="0 0 275 300">
      <circle class="badge__ring" cx="137.5" cy="145" r="127"/>
      <circle class="badge__disc" cx="137.5" cy="145" r="119"/>
      <text class="brand brand__name" x="137.5" y="134" text-anchor="middle" textLength="150" lengthAdjust="spacingAndGlyphs">velmor</text>
      <text class="brand brand__product" x="137.5" y="221" text-anchor="middle" textLength="184" lengthAdjust="spacingAndGlyphs">JUICES</text>
    </svg>
    <ul class="flavours">
      <li><span class="f-serif">KIWI</span> <span class="f-sans">ORANGE</span> <span class="f-brush">APPLE</span></li>
      <li><span class="f-serif">STRAWBERRY</span> <span class="f-serif">BLUEBERRY</span></li>
      <li><span class="f-old">Avocado</span> <span class="f-light">CITRUS</span> <span class="f-brush">GRAPE</span></li>
      <li><span class="f-serif">COCONUT</span> <span class="f-accent">CRANBERRY</span></li>
      <li><span class="f-old">MANGO</span> <span class="f-serif">MELON</span> <span class="f-sans">PEACH</span></li>
      <li><span class="f-brush">PINEAPPLE</span> <span class="f-light">PAPAYA</span></li>
    </ul>
    <div class="rule"></div>
  </section>

  <section class="label label--green">
    <svg class="badge" viewBox="0 0 275 300">
      <circle class="badge__ring" cx="137.5" cy="145" r="127"/>
      <circle class="badge__disc" cx="137.5" cy="145" r="119"/>
      <text class="brand brand__name" x="137.5" y="134" text-anchor="middle" textLength="150" lengthAdjust="spacingAndGlyphs">velmor</text>
      <text class="brand brand__product" x="137.5" y="221" text-anchor="middle" textLength="184" lengthAdjust="spacingAndGlyphs">JUICES</text>
    </svg>
    <ul class="flavours">
      <li><span class="f-serif">KIWI</span> <span class="f-sans">ORANGE</span> <span class="f-brush">APPLE</span></li>
      <li><span class="f-serif">STRAWBERRY</span> <span class="f-serif">BLUEBERRY</span></li>
      <li><span class="f-old">Avocado</span> <span class="f-light">CITRUS</span> <span class="f-brush">GRAPE</span></li>
      <li><span class="f-serif">COCONUT</span> <span class="f-accent">CRANBERRY</span></li>
      <li><span class="f-old">MANGO</span> <span class="f-serif">MELON</span> <span class="f-sans">PEACH</span></li>
      <li><span class="f-brush">PINEAPPLE</span> <span class="f-light">PAPAYA</span></li>
    </ul>
    <div class="rule"></div>
  </section>

</main>
</body>
</html>
```